**** Web design project for VornaSoft ****

For my ICT company VornaSoft I need a website.

We design, build and host web-applications and we have our own CMS product. In the references part we want to show sample websites (thumbnails) + links.

It should look modern (WEB 2.0), rounded corners.

I want the following menu' s:
- Home
- Services
- References
- News
- About VornaSoft
- Contact

Sample websites:
See attachments
http://www.plumvest.com
http://www.gadomirbureauwerk.nl

Reason: Want to take some time for feedback and improvements.

Reason: I'm waiting for a black background, with shadow and ambient light. You'll make a good chance!

Industry/Entity Type

It Company

Requirements
Must have
• - Fixed width (1024px), should fit on an IPad2
- Language selection English/Dutch
- Twitter/Facebook/LinkedIn/RSS icons
- Footer for Terms of use and Copyrights
- Search box
- 3 (or more) boxes for information i.e. news, blog or advertisements
Nice to have
• - Footer Site Map
- Contrasting background outside borders
- wide image (rotator) (with transperant sentence block)
- Shadow

```html
<!DOCTYPE html>
<html lang="en">
<head>
<meta charset="utf-8">
<title>VornaSoft</title>
<link rel="stylesheet" href="https://fonts.googleapis.com/css2?family=Source+Sans+3:wght@400;600&display=swap">
<style>
:root{
  --blue:#2f8fd0;
  --blue-light:#5cb3ea;
  --blue-mid:#3aa0e3;
  --blue-dark:#2b8ad0;
  --nav-top:#55b8ee;
  --nav-bottom:#2a8cd2;
  --ink:#444;
  --slate:#4f6f80;
  --grey-panel:#5e5e5e;
  --footer:#383838;
  --white:#fff;
}
*{margin:0;padding:0;box-sizing:border-box}
html,body{width:1117px;height:1200px;overflow:hidden;background:#fff}
body{font-family:"Source Sans 3",sans-serif;color:var(--ink)}
.page{position:relative;width:1024px;height:1100px;transform:scale(1.0908);transform-origin:0 0;overflow:hidden}
.abs{position:absolute}

.header{left:0;top:0;width:1024px;height:139px;background:linear-gradient(#fff,#f6f7f9);border-bottom:1px solid #e6e8eb}
.brand{left:35px;top:30px;display:flex;align-items:center;gap:14px}
.brand-dot{width:70px;height:70px;border-radius:50%;background:var(--blue-mid)}
.brand-name{font-size:32px;font-weight:400;color:var(--slate);letter-spacing:.5px}
.lang{top:35px;width:24px;height:24px;border-radius:50%;box-shadow:0 1px 2px rgba(0,0,0,.3);overflow:hidden}
.search-field{left:754px;top:84px;width:168px;height:28px;border:1px solid #cfd3d7;background:#fff;font-size:11px;font-style:italic;color:#9aa;padding:7px 14px}
.search-btn{left:928px;top:84px;width:64px;height:28px;background:linear-gradient(#6cc4f4,#3ea6ea);border-radius:2px}

.nav{left:33px;top:147px;width:960px;height:48px;border-radius:8px;background:linear-gradient(var(--nav-top),var(--nav-bottom));box-shadow:0 3px 4px rgba(0,0,0,.25)}
.nav-item{top:0;height:48px;line-height:48px;color:#fff;font-size:14px;padding:0 20px;border-right:1px solid rgba(0,0,0,.12)}
.nav-item.active{background:rgba(0,0,0,.08);border-radius:8px 0 0 8px}
.social{top:155px;width:32px;height:32px;border-radius:50%;background:#fff;box-shadow:0 1px 3px rgba(0,0,0,.3)}

.slider{left:48px;top:208px;width:932px;height:312px;background:#fff;box-shadow:0 6px 10px rgba(0,0,0,.12)}
.slide-photo{left:72px;top:224px;width:886px;height:280px;background:linear-gradient(100deg,#e8ecef 30%,#c9d3dc 60%,#3b4050 85%,#e9eef2)}
.slide-caption{left:72px;top:224px;width:257px;height:280px;background:rgba(95,95,95,.95);color:#fff;padding:44px 22px 0 28px}
.slide-caption h2{font-size:24px;font-weight:600;margin-bottom:14px}
.slide-caption p{font-size:15px;line-height:22px;color:#e6e6e6}
.dots{position:absolute;left:59px;top:212px;display:flex;gap:17px}
.dots span{width:13px;height:13px;border-radius:50%;background:#d8d8d8}
.dots span.on{background:#5cb3ea}

.info-box{top:545px;width:306px;height:140px;border-radius:7px;color:#fff;padding:8px 16px 0 18px;box-shadow:0 2px 3px rgba(0,0,0,.2)}
.info-box h3{font-size:20px;font-weight:600;padding-bottom:6px;border-bottom:2px dotted rgba(255,255,255,.8)}
.info-box p{font-size:11.5px;line-height:18px;text-align:justify;margin-top:10px;padding-left:13px;padding-right:2px;position:relative}
.info-box p::before{content:"";position:absolute;left:0;top:5px;border-left:5px solid #fff;border-top:4px solid transparent;border-bottom:4px solid transparent}
.view-all{position:absolute;right:16px;bottom:0;width:82px;height:23px;border-radius:10px 10px 0 0;background:linear-gradient(#d9eefb,#b8dcf3);color:#1f5f8c;font-size:12px;line-height:23px;padding-left:14px}

.welcome{left:40px;top:700px;width:948px;height:182px;background:linear-gradient(#fff,#eef2f7)}
.welcome h2{position:absolute;left:22px;top:12px;font-size:22px;font-weight:600;color:var(--slate)}
.welcome h2 span{color:var(--blue)}
.welcome p{position:absolute;left:21px;top:56px;width:726px;font-size:11.5px;line-height:22px;text-align:justify}
.welcome-photo{left:770px;top:0;width:178px;height:182px;background:linear-gradient(#f3f5f8,#d9dfe6)}

.services h2{position:absolute;left:59px;top:896px;font-size:19px;font-weight:600;color:var(--blue)}
.svc{font-size:12.5px;color:#444;padding-left:15px}
.svc::before{content:"";position:absolute;left:0;top:4px;border-left:5px solid #555;border-top:4px solid transparent;border-bottom:4px solid transparent}

.newsletter{left:644px;top:901px;width:345px;height:100px;border-radius:8px;background:var(--grey-panel)}
.newsletter h3{position:absolute;left:69px;top:13px;font-size:17px;font-weight:400;color:#fff}
.mail-icon{left:24px;top:12px}
.mail-field{left:25px;top:52px;width:218px;height:28px;background:#fff;font-size:11px;font-style:italic;color:#aaa;padding:7px 14px}
.submit{left:251px;top:52px;width:77px;height:28px;background:linear-gradient(#fff,#b9ddf5);color:#1f5f8c;font-size:14px;font-weight:600;font-style:italic;text-align:center;line-height:28px}

.footer{left:0;top:1022px;width:1024px;height:78px;background:var(--footer);border-top:3px solid #d7d9dc;text-align:center;color:#cfcfcf;font-size:11.5px;font-family:"Source Sans 3",sans-serif}
.footer-links{margin-top:17px}
.footer-links span{padding:0 9px}
.copyright{margin-top:10px}
</style>
</head>
<body>
<div class="page">

  <header class="header abs">
    <div class="brand abs"><div class="brand-dot"></div><div class="brand-name">VornaSoft</div></div>
    <svg class="lang abs" style="left:930px" viewBox="0 0 24 24" role="img" aria-label="English">
      <rect width="24" height="24" fill="#1f3d8c"/><rect x="10" width="4" height="24" fill="#fff"/><rect y="10" width="24" height="4" fill="#fff"/><rect x="10.8" width="2.4" height="24" fill="#d22"/><rect y="10.8" width="24" height="2.4" fill="#d22"/>
    </svg>
    <svg class="lang abs" style="left:968px" viewBox="0 0 24 24" role="img" aria-label="Nederlands">
      <rect width="24" height="8" fill="#c8202f"/><rect y="8" width="24" height="8" fill="#fff"/><rect y="16" width="24" height="8" fill="#21468b"/>
    </svg>
    <div class="search-field abs">Search</div>
    <svg class="search-btn abs" viewBox="0 0 64 28">
      <circle cx="30" cy="12" r="5" fill="none" stroke="#fff" stroke-width="2.5"/><line x1="33.5" y1="15.5" x2="38" y2="20" stroke="#fff" stroke-width="3" stroke-linecap="round"/>
    </svg>
  </header>

  <nav class="nav abs">
    <div class="nav-item active abs" style="left:0;width:88px;padding-left:31px">Home</div>
    <div class="nav-item abs" style="left:88px">Services</div>
    <div class="nav-item abs" style="left:177px">References</div>
    <div class="nav-item abs" style="left:282px">News</div>
    <div class="nav-item abs" style="left:355px">About VornaSoft</div>
    <div class="nav-item abs" style="left:482px;border-right:0">Contact us</div>
  </nav>
  <div class="social abs" style="left:810px" role="img" aria-label="Social network link"></div>
  <div class="social abs" style="left:856px" role="img" aria-label="Social network link"></div>
  <div class="social abs" style="left:902px" role="img" aria-label="Professional network link"></div>
  <div class="social abs" style="left:948px" role="img" aria-label="News feed link"></div>

  <section class="slider abs"></section>
  <div class="slide-photo abs" role="img" aria-label="Team of four business people looking upward in a bright office"></div>
  <div class="slide-caption abs">
    <h2>Inventore Veritatis</h2>
    <p>Sed ut perspiciatis unde omnis iste natus error sit voluptatem accusan tium doloremque lau dantium.</p>
    <div class="dots"><span></span><span></span><span class="on"></span><span></span><span></span></div>
  </div>

  <section class="info-box abs" style="left:40px;background:var(--blue-light)">
    <h3>Latest News</h3>
    <p>Neque porro quisquam est, qui dolorem ipsum quia dolor sit amet, consectetur, adipisci velit, sed quia non numquam eius modi tempora.</p>
    <div class="view-all">View all &raquo;</div>
  </section>
  <section class="info-box abs" style="left:362px;background:var(--blue-mid)">
    <h3>Blog Posts</h3>
    <p>Neque porro quisquam est, qui dolorem ipsum quia dolor sit amet, consectetur, adipisci velit, sed quia non numquam eius modi tempora.</p>
    <div class="view-all">View all &raquo;</div>
  </section>
  <section class="info-box abs" style="left:683px;background:var(--blue-dark)">
    <h3>Advertisment</h3>
    <p>Neque porro quisquam est, qui dolorem ipsum quia dolor sit amet, consectetur, adipisci velit, sed quia non numquam eius modi tempora.</p>
    <div class="view-all">View all &raquo;</div>
  </section>

  <section class="welcome abs">
    <h2>Welcome to <span>VornaSoft</span></h2>
    <p>Sed ut perspiciatis unde omnis iste natus error sit voluptatem accusantium doloremque laudantium, totam rem aperiam, eaque ipsa quae ab illo inventore veritatis et quasi architecto beatae vitae dicta sunt explicabo. Nemo enim ipsam voluptatem quia voluptas sit aspernatur aut odit aut fugit, sed quia consequuntur magni dolores eos qui ratione voluptatem sequi nesciunt. Neque porro quisquam est, qui dolorem ipsum quia dolor sit amet, consectetur, adipisci velit, sed quia non numquam eius modi tempora incidunt ut labore et dolore magnam aliquam quaerat voluptatem. Ut enim ad minima veniam, quis nostrum exercitationem ullam corporis suscipit laboriosam, nisi ut aliquid.</p>
    <div class="welcome-photo abs" role="img" aria-label="Smiling businessman leaning on a desk beside a laptop"></div>
  </section>

  <section class="services">
    <h2>Our Services</h2>
    <div class="svc abs" style="left:60px;top:933px">Nunc convallis enim</div>
    <div class="svc abs" style="left:60px;top:959px">Nulla faucibusNullam</div>
    <div class="svc abs" style="left:60px;top:985px">Nisl egetio vitae</div>
    <div class="svc abs" style="left:260px;top:933px">Mauris iddui necnunc</div>
    <div class="svc abs" style="left:260px;top:960px">Fusce convallis tellus</div>
    <div class="svc abs" style="left:260px;top:987px">Sed volutpat dolor</div>
    <div class="svc abs" style="left:453px;top:933px">Cras iaculis odio</div>
    <div class="svc abs" style="left:453px;top:965px">Mauris eget lorem ipsum</div>
  </section>

  <section class="newsletter abs">
    <svg class="mail-icon abs" width="36" height="26" viewBox="0 0 36 26">
      <rect x="1" y="1" width="34" height="24" fill="#f2f2f2" stroke="#bbb"/><polyline points="1,1 18,14 35,1" fill="none" stroke="#aaa" stroke-width="1.5"/>
    </svg>
    <h3>Signup for NewsLetter</h3>
    <div class="mail-field abs">Enter your mail ID</div>
    <div class="submit abs">SUBMIT</div>
  </section>

  <footer class="footer abs">
    <div class="footer-links"><span>Home</span>|<span>Services</span>|<span>References</span>|<span>News</span>|<span>About VornaSoft</span>|<span>Contactus</span></div>
    <div class="copyright">Copyright &copy; 2012 www.vornasoft.com &nbsp; All rights reserved.</div>
  </footer>

</div>
</body>
</html>
```